Flyer-Design für Verlegung von fugenlosen Böden
Zielgruppe
Die Firma KORVAL, hat seinen Hauptaugenmerk auf das verlegen von fugenlosen Böden gelegt.
welchen Vorteil bietet Ihnen dieser Bodenbelag? Der fugenlose Bodenbelag wie der Epoxidharzboden oder der Steinteppich ist in den letzten Jahren eine beliebte Alternative zu Laminat, Fliesen, Parkett und anderen Bodenbelägen geworden.Seine steigende Beliebtheit verdankt der fugenlose Bodenbelag unter anderem seiner Robustheit.Unsere Bodenbeläge sind Geruchsneutral und bietet eine lange Lebensdauer. Die Zielgruppe sind Private sowie Gewerbliche Kunden.
Aufgabenstellung
Der Text sollte den effekt, 'Wow' das muss ich haben beim Leser auslösen. Das gleiche zählt für die verwendeten Bilder die der Desinger gerne auswählen derf. Mehr Infos Z.b Logo kann sich der Desinger auf der Webseite entnehmen.
www.korval-estrich.example

```html
<!DOCTYPE html>
<html lang="de">
<head>
<meta charset="utf-8">
<title>KORVAL Designböden – Flyer</title>
<link rel="stylesheet" href="https://fonts.googleapis.com/css2?family=Roboto+Condensed:wght@400;700&family=Source+Sans+3:wght@400;600;700&display=swap">
<style>
  :root {
    --orange: #c44a0a;
    --ink: #0d0d0d;
    --white: #ffffff;
    --slate: #454a4f;
    --band: #dcdfe0;
    --photo-light: #dfe3e4;
    --photo-mid: #b9bec0;
    --photo-dark: #8e9597;
  }
  * { box-sizing: border-box; margin: 0; padding: 0; }
  html, body { width: 1200px; height: 846px; overflow: hidden; background: var(--white); }
  .flyer { position: relative; width: 1200px; height: 846px; background: var(--white); overflow: hidden; }

  .headline {
    position: absolute; left: 54px; top: 26px;
    font-family: "Roboto Condensed", sans-serif; font-weight: 400;
    font-size: 57px; line-height: 67px; color: var(--ink); letter-spacing: -0.3px;
    white-space: nowrap;
  }
  .headline strong { color: var(--orange); font-weight: 700; }

  .benefits {
    position: absolute; left: 0; top: 189px; width: 338px; height: 657px;
    background: var(--orange); list-style: none;
  }
  .benefit {
    position: absolute; left: 52px; display: flex; align-items: center;
    transform: translateY(-50%);
    font-family: "Source Sans 3", sans-serif; font-size: 28px; line-height: 34px;
    color: var(--white); white-space: nowrap;
  }
  .benefit svg { width: 46px; height: 40px; flex: none; margin-right: 23px; }

  .scene {
    position: absolute; left: 338px; top: 189px; width: 862px; height: 488px;
    background:
      linear-gradient(100deg, transparent 40%, rgba(255,255,255,.45) 55%, transparent 70%),
      linear-gradient(160deg, var(--photo-light) 0%, var(--photo-mid) 55%, var(--photo-dark) 100%);
  }
  .artworks { position: absolute; left: 397px; top: 379px; display: flex; }
  .artwork { width: 250px; height: 251px; }
  .artwork--blue { width: 252px; background: radial-gradient(circle at 40% 50%, #3fc7f0 0%, #1a3f5c 40%, #1b2632 100%); }
  .artwork--mono { background: radial-gradient(circle at 55% 45%, #ffffff 0%, #6a6a6a 45%, #111 70%, #f2f2f2 100%); }
  .artwork--red { width: 248px; background: radial-gradient(circle at 55% 45%, #7ad04a 0%, #d2261a 50%, #e2a21a 80%, #1a0a05 100%); }

  .brand-band {
    position: absolute; left: 338px; top: 677px; width: 862px; height: 169px;
    background: var(--band);
  }
  .brand-name {
    position: absolute; left: 358px; top: 716px;
    font-family: "Source Sans 3", sans-serif; font-weight: 700;
    font-size: 72px; line-height: 72px; color: var(--slate);
  }

  .claim {
    position: absolute; right: 46px; top: 702px; text-align: right;
    font-family: "Source Sans 3", sans-serif; color: var(--slate);
  }
  .claim-title { font-weight: 700; font-size: 30px; line-height: 38px; color: var(--orange); margin-right: 14px; }
  .claim-text { font-size: 32px; line-height: 39px; }
</style>
</head>
<body>
<main class="flyer">
  <h1 class="headline">
    Unser <strong>Boden hat keine Fugen.</strong><br>
    Er hat <strong>Stil</strong> und ist zudem <strong>robust</strong> und <strong>pflegeleicht!</strong>
  </h1>

  <ul class="benefits">
    <li class="benefit" style="top:78px"><svg viewBox="0 0 46 40"><circle cx="20" cy="21" r="17" fill="none" stroke="#fff" stroke-width="3.5"/><path d="M11 20 L19 30 L44 3" fill="none" stroke="#fff" stroke-width="4" stroke-linecap="round" stroke-linejoin="round"/></svg><span>Der Boden der<br>Zukunft</span></li>
    <li class="benefit" style="top:178px"><svg viewBox="0 0 46 40"><circle cx="20" cy="21" r="17" fill="none" stroke="#fff" stroke-width="3.5"/><path d="M11 20 L19 30 L44 3" fill="none" stroke="#fff" stroke-width="4" stroke-linecap="round" stroke-linejoin="round"/></svg><span>Pflegeleicht und<br>Nachhaltig</span></li>
    <li class="benefit" style="top:280px"><svg viewBox="0 0 46 40"><circle cx="20" cy="21" r="17" fill="none" stroke="#fff" stroke-width="3.5"/><path d="M11 20 L19 30 L44 3" fill="none" stroke="#fff" stroke-width="4" stroke-linecap="round" stroke-linejoin="round"/></svg><span>Kreative<br>Gestaltung</span></li>
    <li class="benefit" style="top:381px"><svg viewBox="0 0 46 40"><circle cx="20" cy="21" r="17" fill="none" stroke="#fff" stroke-width="3.5"/><path d="M11 20 L19 30 L44 3" fill="none" stroke="#fff" stroke-width="4" stroke-linecap="round" stroke-linejoin="round"/></svg><span>Für Fussboden-<br>heizung geeignet</span></li>
    <li class="benefit" style="top:468px"><svg viewBox="0 0 46 40"><circle cx="20" cy="21" r="17" fill="none" stroke="#fff" stroke-width="3.5"/><path d="M11 20 L19 30 L44 3" fill="none" stroke="#fff" stroke-width="4" stroke-linecap="round" stroke-linejoin="round"/></svg><span>LÖSEMITTELFREI</span></li>
    <li class="benefit" style="top:548px"><svg viewBox="0 0 46 40"><circle cx="20" cy="21" r="17" fill="none" stroke="#fff" stroke-width="3.5"/><path d="M11 20 L19 30 L44 3" fill="none" stroke="#fff" stroke-width="4" stroke-linecap="round" stroke-linejoin="round"/></svg><span>FÜR ALLERGIKER<br>GEEIGNET</span></li>
  </ul>

  <div class="scene" role="img" aria-label="Heller, glänzender fugenloser Boden mit Lichtreflexen im Raum"></div>

  <div class="artworks">
    <div class="artwork artwork--blue" role="img" aria-label="Bodenmuster mit hellblauen Farbschlieren auf dunklem Grund"></div>
    <div class="artwork artwork--mono" role="img" aria-label="Bodenmuster mit schwarzen und weißen Farbwirbeln"></div>
    <div class="artwork artwork--red" role="img" aria-label="Bodenmuster mit roten, grünen und gelben Farbverläufen"></div>
  </div>

  <div class="brand-band"></div>
  <div class="brand-name">KORVAL</div>

  <div class="claim">
    <p class="claim-title">KORVAL&nbsp; Designböden</p>
    <p class="claim-text">Ihre perfekte fugenlose<br>Bodenbeschichtung</p>
  </div>
</main>
</body>
</html>
```